TBNW site redesign

Please redesign a home page with content provided. PSD only - no coding
Can use any images from Vexelmarq.com

Please create a site design that more clearly illustrates the client's services and expertise. We are looking for a high-end design.

Any images used must be generic or of Dallas TX.

Fonts: Any
Colors: Match to logo
Look: Modern - Professional

Target Market(s)

medium-large business owners

Number of Pages Required

1 page

Font styles to use
Serif
Sans Serif

Requirements
Must have
• cohesive professional design
• high end look
• Match to logo

```html
<!DOCTYPE html>
<html lang="en">
<head>
<meta charset="utf-8">
<title>TBNW – Commercial Tenant Representation</title>
<link href="https://fonts.googleapis.com/css2?family=Libre+Baskerville:wght@400;700&family=Open+Sans:wght@400;600;700&display=swap" rel="stylesheet">
<style>
:root{
  --red:#c4070d;
  --red-dark:#9e0308;
  --ink:#1b1b1b;
  --grey-text:#6a6a6a;
  --paper:#ffffff;
  --mist:#efefef;
  --serif:"Libre Baskerville", Georgia, serif;
  --sans:"Open Sans", Arial, sans-serif;
}
*{box-sizing:border-box;margin:0;padding:0}
html,body{width:1200px;height:3422px;overflow:hidden}
body{position:relative;background:var(--paper);font-family:var(--sans);color:var(--ink)}
.abs{position:absolute}
.serif{font-family:var(--serif)}
.btn{position:absolute;background:var(--red);color:#fff;font-family:var(--serif);font-weight:700;font-size:17px;letter-spacing:.5px;display:flex;align-items:center;justify-content:center;border-radius:4px;text-transform:uppercase;white-space:nowrap}
.accent{color:var(--red)}

/* header */
.topbar{left:0;top:0;width:1200px;height:103px;background:linear-gradient(90deg,var(--red-dark),var(--red) 40%,var(--red))}
.brand{left:78px;top:22px;height:58px;display:flex;align-items:center;gap:14px;color:#fff;font-family:var(--serif);font-weight:700;font-size:36px;letter-spacing:2px}
.brand-mark{width:22px;height:22px;background:#fff}
.call{right:78px;top:24px;display:flex;align-items:center;gap:18px;color:#fff}
.call small{display:block;font-size:14px;color:#ffd6d6}
.call strong{display:block;font-family:var(--serif);font-size:27px}
.nav{left:0;top:103px;width:1200px;height:64px;background:#fff;border-bottom:1px solid #ddd}
.nav ul{position:absolute;left:92px;top:0;height:64px;display:flex;align-items:center;gap:36px;list-style:none;font-size:15px;text-transform:uppercase}
.search{left:780px;top:111px;width:342px;height:50px;border:1px solid #ccc;display:flex;align-items:center;justify-content:space-between;padding:0 14px;font-size:14px;color:#999}

/* hero */
.hero{left:0;top:167px;width:1200px;height:529px;background:linear-gradient(160deg,#6f7d88 0%,#2f3a44 35%,#58636c 60%,#1f272e 100%)}
.hero-title{left:0;top:300px;width:1200px;text-align:center;color:#fff;font-family:var(--serif);font-size:42px;line-height:62px;font-weight:400}
.hero-sub{left:0;top:434px;width:1200px;text-align:center;color:#fff;font-weight:700;font-size:17px}
.hero-btn{left:445px;top:486px;width:310px;height:57px}

/* why */
.section-title{left:0;width:1200px;text-align:center;font-family:var(--serif);font-size:33px;font-weight:400;text-transform:uppercase}
.feature{width:250px;text-align:center}
.feature .icon{margin:0 auto;width:121px;height:121px;border:3px solid var(--red);display:flex;align-items:center;justify-content:center}
.feature h3{margin-top:34px;font-family:var(--serif);font-size:16px;font-weight:400;text-transform:uppercase}
.feature p{margin:10px auto 0;width:225px;font-size:13px;line-height:22px;color:var(--grey-text)}

/* welcome */
.welcome{left:0;top:1209px;width:1200px;height:461px;background:linear-gradient(180deg,#15161e 0%,#22242e 60%,#3a2e2a 100%)}
.video{left:78px;top:1278px;width:438px;height:296px;background:linear-gradient(150deg,#3d6fa7,#9fc0de 55%,#4b5866)}
.welcome-title{left:563px;top:1270px;color:#fff;font-family:var(--serif);font-size:34px;font-weight:400}
.welcome-copy{left:563px;top:1333px;width:590px;color:#b8b8be;font-size:13px;line-height:26px}
.welcome-copy p+p{margin-top:12px}
.calc-btn{left:566px;top:1522px;width:271px;height:54px}

/* testimonial */
.testimonial{left:0;top:1670px;width:1200px;height:196px;background:var(--red)}
.quote-badge{left:79px;top:1721px;width:62px;height:62px;border-radius:50%;background:#fff;color:var(--red);font-family:var(--serif);font-size:60px;line-height:90px;text-align:center}
.avatar{left:146px;top:1702px;width:100px;height:100px;border-radius:50%;border:4px solid #fff;background:linear-gradient(180deg,#d9c7b6,#8a7567)}
.quote-text{left:274px;top:1702px;width:850px;color:#fff;font-size:13px;line-height:29px}
.quote-name{right:82px;top:1812px;color:#fff;font-family:var(--serif);font-weight:700;font-size:19px}

/* cta */
.cta-brand{left:524px;top:1912px;width:152px;height:84px;background:var(--red);color:#fff;font-family:var(--serif);font-weight:700;font-size:34px;letter-spacing:2px;display:flex;align-items:center;justify-content:center}
.cta-text{left:0;top:2012px;width:1200px;text-align:center;font-family:var(--serif);font-size:24px;line-height:38px;color:#333}
.cta-btn{left:439px;top:2106px;width:322px;height:52px}

/* articles */
.articles{left:0;top:2220px;width:1200px;height:365px;background:var(--mist)}
.article-img{width:207px;height:171px}
.article-text{width:250px;display:flex;flex-direction:column;gap:8px}
.article-title{font-family:var(--serif);font-size:16px;line-height:33px;color:#222}
.article-tag{font-size:15px;color:var(--red)}

/* contact */
.contact{left:0;top:2585px;width:1200px;height:627px;background:linear-gradient(180deg,#2c2a2a 0%,#3d3530 45%,#1d1b1d 100%)}
.contact-title{left:0;top:2645px;width:1200px;text-align:center;font-family:var(--serif);font-size:38px;font-weight:400;color:#fff}
.col-title{font-family:var(--serif);font-size:24px;font-weight:400;color:#fff;text-transform:uppercase;white-space:nowrap}
.field{left:78px;width:499px;background:#fff;border:2px solid var(--red);font-size:13px;color:#666;padding:14px 16px}
.submit{left:264px;top:3045px;width:124px;height:124px;border-radius:50%;background:var(--red);color:#fff;font-family:var(--serif);font-weight:700;font-size:18px;display:flex;align-items:center;justify-content:center}
.info{left:730px;display:flex;gap:16px;color:#ddd;font-size:14px;line-height:27px}
.social{top:3005px;width:42px;height:42px;border-radius:50%;border:2px solid #ccc}

/* footer */
.footer{left:0;top:3212px;width:1200px;height:210px;background:var(--red)}
.footer-line{left:0;width:1200px;text-align:center;color:#fff;font-size:14px}
</style>
</head>
<body>

<header>
  <div class="abs topbar"></div>
  <div class="abs brand"><span class="brand-mark"></span>TBNW</div>
  <div class="abs call">
    <svg width="44" height="44" viewBox="0 0 24 24" aria-hidden="true"><path fill="#fff" d="M6.6 10.8a15.1 15.1 0 0 0 6.6 6.6l2.2-2.2c.3-.3.7-.4 1-.2 1.1.4 2.3.6 3.6.6.6 0 1 .4 1 1V20c0 .6-.4 1-1 1A17 17 0 0 1 3 4c0-.6.4-1 1-1h3.5c.6 0 1 .4 1 1 0 1.3.2 2.5.6 3.6.1.3 0 .7-.2 1z"/></svg>
    <div><small>Call Today</small><strong>214-555-0142</strong></div>
  </div>
  <nav class="abs nav">
    <ul>
      <li><svg width="18" height="16" viewBox="0 0 18 16" aria-label="Home"><path fill="#c4070d" d="M9 0 0 8h2.5v8h5v-5h3v5h5V8H18z"/></svg></li>
      <li>Services</li><li>About TBNW</li><li>Contact Us</li><li>Blog</li><li>Market News</li>
    </ul>
  </nav>
  <div class="abs search"><span>Search...</span>
    <svg width="20" height="20" viewBox="0 0 20 20" aria-hidden="true"><circle cx="8" cy="8" r="6" fill="none" stroke="#222" stroke-width="2.5"/><path d="m12.5 12.5 6 6" stroke="#222" stroke-width="3"/></svg>
  </div>
</header>

<section>
  <div class="abs hero" role="img" aria-label="Downtown Dallas glass skyscrapers seen from street level"></div>
  <svg class="abs" style="left:0;top:640px" width="1200" height="80" viewBox="0 0 1200 80" aria-hidden="true">
    <path d="M0 30 Q600 60 1200 30 L1200 56 L0 56Z" fill="#c4070d"/>
    <path d="M0 44 Q600 74 1200 44 L1200 80 L0 80Z" fill="#fff"/>
    <path d="M540 60 Q545 22 600 22 Q655 22 660 60Z" fill="#c4070d"/>
    <circle cx="583" cy="45" r="5" fill="none" stroke="#fff" stroke-width="2"/>
    <circle cx="600" cy="45" r="5" fill="none" stroke="#fff" stroke-width="2"/>
    <circle cx="617" cy="45" r="5" fill="#fff"/>
  </svg>
  <h1 class="abs hero-title">TBNW –The Best Commercial Tenant<br>Reps in Dallas TX!</h1>
  <p class="abs hero-sub">Let Us Handle Your Commercial Real Estate Lease Negotiations!</p>
  <div class="btn hero-btn">Contact TBNW Today !</div>
</section>

<section>
  <h2 class="abs section-title" style="top:792px">Why Tenant <span class="accent">Representation?</span></h2>
  <div class="abs feature" style="left:76px;top:866px">
    <div class="icon"><svg width="76" height="50" viewBox="0 0 76 50" aria-hidden="true"><path fill="#c4070d" d="M2 10 18 4l10 8 12-6 10 4 8-6 16 8-4 16-10 4-10 12-6-4-4 4-6-4-4 3-6-4-4 2-6-6-6-3 2-8z"/><path d="M30 18 42 28M36 30l6 5M28 32l6 5M22 34l5 4" stroke="#fff" stroke-width="2.5"/></svg></div>
    <h3>Relationships</h3>
    <p>Save time by trusting TBNW year after year to find the right location for you Once we've worked.</p>
  </div>
  <div class="abs feature" style="left:343px;top:866px">
    <div class="icon"><svg width="60" height="60" viewBox="0 0 60 60" aria-hidden="true"><rect x="4" y="14" width="40" height="42" rx="3" fill="#c4070d"/><rect x="14" y="4" width="42" height="42" rx="3" fill="#fff" stroke="#c4070d" stroke-width="4"/><path d="M35 13v24M23 25h24" stroke="#c4070d" stroke-width="6"/></svg></div>
    <h3>Access to More</h3>
    <p>We have no agreements or personal incentives for specific properties, so we can.</p>
  </div>
  <div class="abs feature" style="left:610px;top:866px">
    <div class="icon"><svg width="54" height="66" viewBox="0 0 54 66" aria-hidden="true"><rect x="3" y="8" width="48" height="56" rx="3" fill="#c4070d"/><rect x="17" y="2" width="20" height="12" rx="2" fill="#c4070d" stroke="#fff" stroke-width="2"/><rect x="11" y="20" width="32" height="38" fill="#fff"/><path d="M15 28h24M15 35h24M15 42h24M15 49h24" stroke="#c4070d" stroke-width="2.5"/></svg></div>
    <h3>Free to You</h3>
    <p>You pay us nothing. We get our commission from the property being leased.</p>
  </div>
  <div class="abs feature" style="left:874px;top:866px">
    <div class="icon"><svg width="62" height="62" viewBox="0 0 62 62" aria-hidden="true"><circle cx="34" cy="20" r="14" fill="#c4070d"/><path d="M14 62c0-16 9-24 20-24s20 8 20 24z" fill="#c4070d"/><path d="M18 22a16 16 0 0 1 32 0" fill="none" stroke="#c4070d" stroke-width="3"/><rect x="8" y="20" width="12" height="16" rx="4" fill="#c4070d"/></svg></div>
    <h3>Customized Service</h3>
    <p>Aside from saving you the time of repeating what your needs are to each new location.</p>
  </div>
</section>

<section>
  <div class="abs welcome" role="img" aria-label="Dallas skyline at night"></div>
  <svg class="abs" style="left:0;top:1200px" width="1200" height="30" viewBox="0 0 1200 30" aria-hidden="true">
    <path d="M0 0H1200V12Q600 -6 0 22Z" fill="#fff"/>
    <path d="M0 22Q600 -6 1200 12V18Q600 2 0 28Z" fill="#c4070d"/>
  </svg>
  <div class="abs video" role="img" aria-label="Business handshake in front of city towers, video still"></div>
  <svg class="abs" style="left:273px;top:1389px" width="58" height="56" viewBox="0 0 58 56" aria-label="Play video"><rect width="58" height="56" rx="12" fill="#d4161b"/><path d="M22 15v26l20-13z" fill="#fff"/></svg>
  <h2 class="abs welcome-title">WELCOME TO <span class="accent">TBNW</span></h2>
  <div class="abs welcome-copy">
    <p>At TBNW, we focus solely on office and industrial/warehouse commercial real estate leasing and sales in the greater Dallas/Fort Worth area. We believe that our unique commercial office space service and market knowledge is the key to our clients' growth and ultimate business success.</p>
    <p>We strive to learn the specific needs of your company and be an essential team member that will find the best solution for your commercial real estate needs.</p>
  </div>
  <div class="btn calc-btn">Space Calculator</div>
</section>

<section>
  <div class="abs testimonial"></div>
  <div class="abs quote-badge">“</div>
  <div class="abs avatar" role="img" aria-label="Client portrait"></div>
  <p class="abs quote-text">"The real estate team at TBNW has decades of experience in Commercial. One advantage of TBNW is they know all the properties that are about to become available, BEFORE they are available. They have the inside track on properties and they watch your back at the negotiating table. Very impressive with a polished approach. Let the team run with your next project &amp; you won't be disappointed."</p>
  <p class="abs quote-name">— Marcus Allen Whitfield</p>
</section>

<section>
  <div class="abs cta-brand">TBNW</div>
  <p class="abs cta-text">Whether your lease is expiring soon, or you're just starting your search,<br>TBNW can help you find the perfect space.</p>
  <div class="btn cta-btn">Make an Appointment</div>
</section>

<section>
  <div class="abs articles"></div>
  <h2 class="abs section-title" style="top:2280px">Latest <span class="accent">Articles</span></h2>
  <div class="abs article-img" style="left:78px;top:2352px;background:linear-gradient(180deg,#7fa9d6,#c9d8e6 55%,#6d8a5a)" role="img" aria-label="Modern glass office building"></div>
  <div class="abs article-text" style="left:306px;top:2348px">
    <p class="article-title">6 Important Key Aspects of Tenant Representation To Know !</p>
    <p class="article-tag">TBNW</p>
  </div>
  <div class="abs article-img" style="left:598px;top:2352px;background:linear-gradient(150deg,#2f6fb2,#a9c9e8 50%,#4d7fae)" role="img" aria-label="Office towers viewed looking upward"></div>
  <div class="abs article-text" style="left:830px;top:2348px">
    <p class="article-title">How Dose Landlord Recapture Relate To My Office Lease ?</p>
    <p class="article-tag">TBNW</p>
  </div>
</section>

<section>
  <div class="abs contact" role="img" aria-label="Aerial view of Dallas downtown"></div>
  <h2 class="abs contact-title"><span class="accent">CONTACT</span> US</h2>
  <h3 class="abs col-title" style="left:224px;top:2735px">Free Locator</h3>
  <div class="abs field" style="top:2788px;height:52px">Enter Name :</div>
  <div class="abs field" style="top:2849px;height:53px;border-color:#fff">Enter Phone No :</div>
  <div class="abs field" style="top:2911px;height:52px;border-color:#fff">Enter E-Mail :</div>
  <div class="abs field" style="top:2975px;height:135px;border-color:#fff">Message :</div>
  <div class="abs submit">SUBMIT</div>

  <h3 class="abs col-title" style="left:767px;top:2735px">Keep in Touch</h3>
  <div class="abs info" style="top:2794px">
    <svg width="18" height="18" viewBox="0 0 18 18" aria-hidden="true"><path fill="#c4070d" d="M2 18V6l7-5 7 5v12h-5v-5H7v5z"/></svg>
    <div>TBNW<br>412 Cedar Row Avenue, Suite 300,<br>Dallas, TX 75201</div>
  </div>
  <div class="abs info" style="top:2906px">
    <svg width="18" height="18" viewBox="0 0 24 24" aria-hidden="true"><path fill="#c4070d" d="M6.6 10.8a15.1 15.1 0 0 0 6.6 6.6l2.2-2.2c.3-.3.7-.4 1-.2 1.1.4 2.3.6 3.6.6.6 0 1 .4 1 1V20c0 .6-.4 1-1 1A17 17 0 0 1 3 4c0-.6.4-1 1-1h3.5c.6 0 1 .4 1 1 0 1.3.2 2.5.6 3.6.1.3 0 .7-.2 1z"/></svg>
    <div>214 - 555 - 0142</div>
  </div>
  <div class="abs info" style="top:2949px">
    <svg width="18" height="18" viewBox="0 0 18 18" aria-hidden="true"><rect x="1" y="6" width="16" height="11" rx="2" fill="#c4070d"/><rect x="4" y="1" width="10" height="6" fill="#c4070d"/></svg>
    <div>214 - 555 - 0187</div>
  </div>
  <div class="abs social" style="left:727px;background:var(--red);border-color:var(--red)"></div>
  <div class="abs social" style="left:773px"></div>
  <div class="abs social" style="left:819px"></div>
  <div class="abs social" style="left:864px"></div>
</section>

<footer>
  <div class="abs footer"></div>
  <svg class="abs" style="left:548px;top:3164px" width="104" height="50" viewBox="0 0 104 50" aria-label="Back to top"><path d="M0 50 52 0l52 50z" fill="#c4070d"/><path d="M38 30l14-12 14 12M38 40l14-12 14 12" fill="none" stroke="#fff" stroke-width="3"/></svg>
  <p class="abs footer-line" style="top:3248px;text-decoration:underline">State Realty Licensing Board Mandated Disclosure Notices – click links below to view pages</p>
  <p class="abs footer-line" style="top:3282px">State Realty Licensing Board Information About Brokerage Services</p>
  <p class="abs footer-line" style="top:3314px">State Realty Licensing Board Consumer Protection Notice</p>
  <p class="abs footer-line" style="top:3366px">©TBNW - 2018 All Right Reserved.</p>
</footer>

</body>
</html>
```